Dale Hornsby's Swingcraft Big Band — Hot & Sticky ------ CD Cover Art (and Disc Art)

Need a front cover jacket and a disc design for a fantastic all-pro big band (jazz/funk/reggae) CD. We really want to use a group photo somehow since so many of the band members are world famous, LA's finest studio musicians with mostly original music arranged by the biggest names in jazz. Playful, fun, lighthearted, tasteful arrangements with world class soloists.

Target Market(s)

Music/Jazz/Big band enthusiasts; other musicians

Other font styles liked:
• See uploaded file #4

Colors

Designer to choose colors to be used in the design.

Requirements
Must have
• Legibility . . . must be easy to read and not crowded or cluttered. Font idea below (A Quiet Night Beneath The Tangled Pines) is for feel and flavor. It is absolutely not necessary to match if you have something you like better.
Nice to have
• Colorful but not tacky. Maybe a play on the CD title, Hot and Sticky?

```html
<!DOCTYPE html>
<html lang="en">
<head>
<meta charset="utf-8">
<title>Dale Hornsby's Swingcraft Big Band — Hot and Sticky</title>
<link href="https://fonts.googleapis.com/css2?family=Alfa+Slab+One&family=IM+Fell+English&family=Archivo+Black&display=swap" rel="stylesheet">
<style>
  :root{
    --page:#ffffff;
    --brick:#b4683f;
    --brick-dark:#7d3f26;
    --mortar:#c9a07a;
    --paint-purple:#7a3b86;
    --paint-edge:#e9a552;
    --crowd:#4a3328;
    --ink:#0a0a0a;
    --chalk:#f3f1ee;
  }
  html,body{margin:0;padding:0;width:1200px;height:1200px;overflow:hidden;background:var(--page);}
  .canvas{position:relative;width:1200px;height:1200px;}
  .cover{position:absolute;left:86px;top:86px;width:1026px;height:1026px;display:block;}
  .band-name{font-family:"IM Fell English",serif;fill:var(--chalk);}
  .title-hot{font-family:"Alfa Slab One",serif;fill:var(--paint-purple);fill-opacity:.82;stroke:var(--paint-edge);stroke-width:6;paint-order:stroke;}
  .title-and{font-family:"Alfa Slab One",serif;fill:var(--chalk);}
  .title-sticky{font-family:"Alfa Slab One",serif;fill:var(--chalk);stroke:#3a2a22;stroke-width:3;paint-order:stroke;}
  .format-mark,.label-mark{font-family:"Archivo Black",sans-serif;fill:var(--chalk);}
</style>
</head>
<body>
<div class="canvas">
  <svg class="cover" viewBox="0 0 1026 1026" xmlns="http://www.w3.org/2000/svg">
    <defs>
      <linearGradient id="wallTone" x1="0" y1="0" x2="0" y2="1">
        <stop offset="0" stop-color="#b9703f"/>
        <stop offset=".5" stop-color="#a85c36"/>
        <stop offset="1" stop-color="#8a4a2e"/>
      </linearGradient>
      <linearGradient id="crowdTone" x1="0" y1="0" x2="0" y2="1">
        <stop offset="0" stop-color="#5a3b2e" stop-opacity="0"/>
        <stop offset=".15" stop-color="#4a3328"/>
        <stop offset=".75" stop-color="#3a2b26"/>
        <stop offset="1" stop-color="#0a0a0a"/>
      </linearGradient>
    </defs>

    <rect class="wall-photo" x="0" y="0" width="1026" height="920" fill="url(#wallTone)" role="img" aria-label="Painted red brick wall behind the band"/>
    <rect class="group-photo" x="0" y="390" width="1026" height="530" fill="url(#crowdTone)" role="img" aria-label="Group photo of the big band members with their horns, guitars and music stands in the studio"/>

    <text class="band-name" x="513" y="80" text-anchor="middle" font-size="56" textLength="890" lengthAdjust="spacingAndGlyphs">Dale Hornsby's Swingcraft Big Band</text>

    <text class="title-hot" x="490" y="470" text-anchor="middle" font-size="380" textLength="850" lengthAdjust="spacingAndGlyphs">HOT</text>
    <text class="title-and" x="0" y="0" font-size="92" transform="translate(962 160) rotate(90)">and</text>

    <text class="title-sticky" x="513" y="875" text-anchor="middle" font-size="230" textLength="920" lengthAdjust="spacingAndGlyphs">STICKY</text>

    <rect class="footer-band" x="0" y="918" width="1026" height="108" fill="var(--ink)"/>
    <text class="format-mark" x="30" y="982" font-size="24">Clear Tone Audio</text>
    <text class="label-mark" x="992" y="982" text-anchor="end" font-size="24">Bluebell Lane Records</text>
  </svg>
</div>
</body>
</html>
```